Corvale Homes

To produce a business card design for our newly established house building and development company, We have had a logo design done please see attached, our slogan is "building your home sweet home"
Contact Information for Business Card
Adress on card needs to Read - 58 Elmsworth Lane, Stanbridge, Westmoorshire WM24 4QT. Director name Dean Vascotti
Requirements
Must have
- Web adress is www.corvale-homes.co.uk
- Email address is info@corvale-homes.co.uk
- phone number 07700 900417

```html
<!DOCTYPE html>
<html lang="en">
<head>
<meta charset="utf-8">
<title>Corvale Homes – Business Card</title>
<link rel="stylesheet" href="https://fonts.googleapis.com/css2?family=Roboto:wght@400;500;700&family=Roboto+Condensed:wght@700&display=swap">
<style>
  :root {
    --backdrop: #2b2b2b;
    --brand-green: #8dc63f;
    --card-white: #f1f1f1;
    --accent-grey: #8a8a8a;
    --back-grey: #9c9c9c;
    --text-white: #ffffff;
  }
  * { margin: 0; padding: 0; box-sizing: border-box; }
  html, body {
    width: 1200px; height: 960px; overflow: hidden;
    background: var(--backdrop);
    font-family: "Roboto", Arial, sans-serif;
  }
  .canvas { position: relative; width: 1200px; height: 960px; }
  .card { position: absolute; width: 600px; height: 343px; overflow: hidden; }
  .card-front { left: 322px; top: 108px; background: var(--card-white); }
  .card-back { left: 320px; top: 493px; background: var(--back-grey); }
  .front-shapes { position: absolute; inset: 0; }
  .contact-block {
    position: absolute; left: 24px; top: 94px; color: var(--text-white);
  }
  .person-name {
    font-family: "Roboto Condensed", "Arial Narrow", sans-serif;
    font-weight: 700; font-size: 21px; line-height: 24px;
  }
  .person-role {
    font-weight: 500; font-size: 15px; line-height: 17px; margin-left: 2px;
  }
  .address { font-size: 14.5px; line-height: 18px; margin-top: 9px; }
  .contact-list { list-style: none; margin-top: 10px; }
  .contact-list li {
    display: flex; align-items: center; gap: 8px;
    font-size: 14.5px; line-height: 19px;
  }
  .contact-list svg { width: 14px; height: 14px; flex: none; }
  .brand-name-front {
    position: absolute; left: 318px; width: 270px; top: 172px;
    text-align: center; color: var(--brand-green);
    font-weight: 700; font-size: 30px; letter-spacing: 1px; line-height: 36px;
  }
  .brand-name-back {
    position: absolute; left: 0; right: 0; top: 140px; text-align: center;
    color: var(--text-white); font-weight: 700; font-size: 44px; letter-spacing: 2px;
  }
  .back-web {
    position: absolute; left: 0; right: 0; top: 286px; text-align: center;
    color: var(--text-white); font-size: 15px; letter-spacing: 2.6px;
  }
</style>
</head>
<body>
<div class="canvas">
  <section class="card card-front">
    <svg class="front-shapes" viewBox="0 0 600 343" aria-hidden="true">
      <polygon points="0,0 318,0 250,162 330,343 0,343" fill="var(--brand-green)"/>
      <polygon points="318,0 338,0 262,162 340,343 330,343 250,162" fill="var(--accent-grey)"/>
    </svg>
    <div class="contact-block">
      <div class="person-name">DEAN VASCOTTI</div>
      <div class="person-role">DIRECTOR</div>
      <p class="address">58 Elmsworth Lane, Stanbridge<br>Westmoorshire WM24 4QT.</p>
      <ul class="contact-list">
        <li><svg viewBox="0 0 24 24" fill="#fff"><path d="M6.6 10.8a15.1 15.1 0 0 0 6.6 6.6l2.2-2.2c.3-.3.7-.4 1-.2 1.1.4 2.3.6 3.6.6.6 0 1 .4 1 1V20c0 .6-.4 1-1 1A17 17 0 0 1 3 4c0-.6.4-1 1-1h3.5c.6 0 1 .4 1 1 0 1.3.2 2.5.6 3.6.1.3 0 .7-.2 1z"/></svg>07700 900417</li>
        <li><svg viewBox="0 0 24 24" fill="#fff"><path d="M2 5h20v2l-10 6L2 7z M2 9l10 6 10-6v10H2z"/></svg>info@corvale-homes.co.uk</li>
        <li><svg viewBox="0 0 24 24"><circle cx="12" cy="12" r="10" fill="#fff"/><path d="M4 9c3 0 4 2 3 4s1 4 3 4M14 3c-1 3 1 4 3 4s3 2 3 4" fill="none" stroke="var(--brand-green)" stroke-width="2"/></svg>www.corvale-homes.co.uk</li>
      </ul>
    </div>
    <div class="brand-name-front">CORVALE HOMES</div>
  </section>

  <section class="card card-back">
    <div class="brand-name-back">CORVALE HOMES</div>
    <div class="back-web">WWW.CORVALE-HOMES.CO.UK</div>
  </section>
</div>
</body>
</html>
```